Presentation for partners template design for a healthy bakery

A bakery that makes healthy homemade cupcakes, needs a presentation template for wholesale partners. We need 3-4 template pages with pictures and text blocks, one template that can accomodate a pricing table. Just to give you an idea for the templates our final presentation will include:
1. Cover page with logo
2. Intro page about us
3. Detailed description of products
4. Menu table: cupcakes with wholesale pricing
5. Contact page
Updates

Target Market(s)

Food stores, cafés, fitness clubs, pastry shops, etc.

Industry/Entity Type

Bakery

Font styles to use
Sans Serif

Colors
fee3d4
fce8d3
eaf2ce
cadf82
ffffff
000000
cfeae6
ec1f27
86cfc6

Requirements
Must have
• Presentation needs to look serious and professional. The design needs to give an eco feel: we use recycled materials in our packaging and production. Please make sure the fonts you use support Cyrillic.
Nice to have
• The format of pages is either square or horizontal A4. The company mint colour (see logo attached) needs to be used, but other colours can be used in addition (lime green, peach, black, chocolate brown, red, etc). Craft paper texture (like our packaging, see photos) would be nice to have.

```html
<!DOCTYPE html>
<html lang="en">
<head>
<meta charset="utf-8">
<title>My Product</title>
<link rel="stylesheet" href="https://fonts.googleapis.com/css2?family=Dosis:wght@400;500&display=swap">
<style>
  :root {
    --mint: #86cfc6;
    --mint-text: #8fd6c8;
    --mint-pale: #cfeae6;
    --lime: #cadf82;
    --photo-shade: #6c6b70;
  }
  html, body {
    margin: 0;
    padding: 0;
    overflow: hidden;
    background: #ffffff;
  }
  .page {
    position: relative;
    width: 1200px;
    height: 848px;
    overflow: hidden;
    font-family: 'Dosis', sans-serif;
    background: var(--photo-shade);
  }
  .page__photo {
    position: absolute;
    inset: 0;
    background:
      radial-gradient(ellipse 330px 300px at 560px 560px, rgba(170, 165, 180, 0.55), transparent 70%),
      radial-gradient(ellipse 260px 180px at 1000px 110px, rgba(120, 170, 160, 0.5), transparent 70%),
      radial-gradient(ellipse 220px 140px at 990px 280px, rgba(150, 125, 95, 0.45), transparent 70%),
      linear-gradient(160deg, #77767b 0%, #6a696e 45%, #626167 100%);
  }
  .page__bands {
    position: absolute;
    left: 0;
    top: 0;
    width: 420px;
    height: 848px;
  }
  .band--lime { fill: var(--lime); }
  .band--mint { fill: var(--mint-pale); }
  .product {
    position: absolute;
    left: 530px;
    top: 0;
    width: 504px;
    text-align: center;
    color: var(--mint-text);
  }
  .product__title {
    margin: 0;
    position: absolute;
    left: -40px;
    right: -40px;
    top: 144px;
    font-size: 88px;
    font-weight: 400;
    line-height: 1;
    color: var(--mint);
    letter-spacing: 0.5px;
  }
  .product__body {
    position: absolute;
    top: 308px;
    left: 0;
    width: 504px;
    font-size: 17.4px;
    line-height: 24px;
    font-weight: 400;
    hyphens: auto;
  }
  .product__body p { margin: 0; }
</style>
</head>
<body>
<main class="page">
  <div class="page__photo" role="img" aria-label="Close-up photo of cupcakes topped with pastel star sprinkles and piped mint frosting"></div>

  <svg class="page__bands" viewBox="0 0 420 848" aria-hidden="true">
    <path class="band--lime" d="M148 0 L388 0 Q344 300 344 424 Q344 640 348 848 L164 848 Q186 640 186 424 Q186 200 148 0 Z"/>
    <path class="band--mint" d="M216 0 L302 0 Q300 300 300 424 Q300 640 302 848 L224 848 Q232 640 232 424 Q232 200 216 0 Z"/>
  </svg>

  <section class="product">
    <h1 class="product__title">MY PRODUCT</h1>
    <div class="product__body">
      <p>Lorem ipsum dolor sit amet, consectetur adipiscing elit. Nunc ac faucibus ex. Ut ac sodales leo. Sed vitae lectus sit amet risus venenatis rhoncus. Vestibulum et arcu laoreet leo gravida fringilla sed in lorem. Aliquam malesuada, leo nec vulputate ultrices, tortor diam molestie mauris, eu pretium magna libero a elit. Nunc non cursus turpis, vel varius est. Donec sed lorem libero. Duis rutrum ac urna vitae facilisis. Donec dignissim velit eu pulvinar vulputate. Integer non nunc quam.</p>
      <p>Etiam porttitor mauris eros, a dignissim arcu luctus ac. Duis ac placerat odio. Curabitur at nisl at tellus tincidunt tincidunt ac et augue. Etiam diam justo, tincidunt in imperdiet non, ullamcorper in dolor. Pellentesque mi eros, rhoncus sit amet lacus ut, feugiat lacinia risus. Ut pharetra facilisis sem. Vivamus porta lacus lorem, et semper quam laoreet a. Vivamus lacus urna, iaculis ac ultrices ac, lacinia eget turpis. Morbi venenatis, massa et lacinia tincidunt, turpis urna cursus nisl, facilisis egestas tellus turpis a nisi. Proin facilisis, nibh sed finibus feugiat, enim enim vestibulum elit, eu pellentesque justo arcu et enim. Interdum et malesuada fames ac ante ipsum primis in faucibus. Fusce eu turpis iaculis, scelerisque</p>
    </div>
  </section>
</main>
</body>
</html>
```